Ledgerwise Reach - B2B Demand Generation Website Project

We need a fully functional website for www.ledgerwisereach.example. We are a B2B Demand Generation company, based in London, working with companies such as QRT, VKD, Norvex, Brindlow, Tarvo generating them sales leads for their sales teams. We run this through digital marketing newsletter promotions and have a network of websites. Content syndication, data, demand generation, online marketing. Our logo has just been redone (attached) and we have a holding page already which i would like to use the style / colours. Our logo is bright and vibrant but i dont want the site to be a rainbow. We are expensive, classy, professorial, B2B, intelligent.

Home
About Us
Our Services
Prospora & QA Technology
Intent Data
Testimonials
Contact Us
Updates

Target Market(s)

B2B Marketers (QRT, Velquarion, Tarvo, VKD, Opal Reach, Driftmoor, Harlow Quantis, Technology Companies, Data Companies, Marketing Teams, Tumbleden.

Industry/Entity Type

Marketing

Coding

Coded - Design and coding required

Number of Pages Required

5+ page

Font styles to use
Sans Serif

Requirements
Must have
• Home
About Us
Our Services
Prospora & QA Technology
Intent Data
Testimonials
Contact Us

Simple Pages.

Look classy, intelligent, data experts. I like the video homepages were the image moves at the top. Very soft animation.
Nice to have
• Websites i like:

https://www.vkd.example/
https://www.brevantor.example/
https://www.plumfieldsites.example.co.uk/

Ledgerwise Reach - The Demand Generation Company
Should not have
• Glimpsevault crap images

```html
<!DOCTYPE html>
<html lang="en">
<head>
<meta charset="utf-8">
<title>Ledgerwise Reach - The Demand Generation Company</title>
<link rel="stylesheet" href="https://fonts.googleapis.com/css2?family=Poppins:wght@400;500;600;700&family=Open+Sans:wght@400;600&display=swap">
<style>
:root{
  --navy:#0b2a6b;
  --navy-deep:#071c4c;
  --blue:#1f4fa8;
  --ink:#222a36;
  --muted:#7a8190;
  --line:#e3e6ec;
  --soft:#f4f5f7;
  --stage:#eceef1;
  --white:#ffffff;
}
*{box-sizing:border-box;margin:0;padding:0}
html,body{width:1200px;height:2396px;overflow:hidden}
body{background:var(--stage);font-family:"Open Sans",sans-serif;color:var(--ink);position:relative}
h1,h2,h3,h4,.brand,.btn,.nav a{font-family:"Poppins",sans-serif}
.page{position:absolute;left:292px;top:40px;width:616px;height:2262px;background:var(--white);box-shadow:0 6px 24px rgba(20,30,60,.12);overflow:hidden}
.section{position:absolute;left:0;width:616px}
.topbar{top:0;height:16px;background:var(--navy);color:#c9d4ee;font-size:5px;display:flex;align-items:center;justify-content:center}
.header{top:16px;height:64px;display:flex;align-items:center;justify-content:space-between;padding:0 30px}
.brand{font-size:9px;font-weight:600;color:var(--navy)}
.nav{display:flex;gap:14px}
.nav a{font-size:6px;color:var(--ink);text-decoration:none}
.hero{top:80px;height:300px;background:linear-gradient(100deg,#0a1f57,#123a8c 60%,#0d2c72)}
.hero-art{position:absolute;left:0;top:0;width:300px;height:300px;background:linear-gradient(135deg,#0a1f57,#1a3d96 55%,#0d2c72)}
.hero-copy{position:absolute;left:290px;top:80px;width:290px;color:var(--white)}
.hero-copy h1{font-size:21px;line-height:1.15;font-weight:700}
.btn{display:inline-block;background:var(--white);color:var(--navy);font-size:6px;font-weight:600;padding:6px 14px;border-radius:10px;margin-top:14px}
.btn.dark{background:var(--navy);color:var(--white)}
.hero-note{position:absolute;right:30px;bottom:50px;color:#b8c6e8;font-size:5px;width:70px;line-height:1.5}
h2{font-size:13px;font-weight:600;text-align:center;color:var(--ink)}
.sub{font-size:5.5px;color:var(--muted);text-align:center;margin-top:4px}
.clients{top:400px;height:220px;padding-top:20px}
.stats{display:flex;justify-content:center;gap:22px;margin-top:22px}
.stat{width:112px;height:48px;border:1px solid var(--line);border-radius:3px;text-align:center;padding-top:10px}
.stat b{font-family:"Poppins",sans-serif;font-size:11px;color:var(--navy)}
.stat span{display:block;font-size:5px;color:var(--muted);margin-top:2px}
.logos{display:flex;justify-content:center;gap:22px;margin-top:30px;font-family:"Poppins",sans-serif;font-size:7px;font-weight:600;color:#a3a8b3}
.split{height:250px;background:var(--soft)}
.split.white{background:var(--white)}
.split .copy{position:absolute;top:60px;width:220px}
.split h3{font-size:11px;font-weight:600;margin-bottom:8px}
.split p{font-size:5px;line-height:1.7;color:var(--muted)}
.photo{position:absolute;top:50px;width:230px;height:160px}
.about{top:630px}
.services{top:880px;height:252px;text-align:center;padding-top:42px}
.svc-row{display:flex;justify-content:center;gap:70px;margin-top:24px}
.svc{width:90px}
.svc-icon{width:40px;height:40px;border-radius:50%;border:1px solid var(--line);margin:0 auto;display:flex;align-items:center;justify-content:center}
.svc-icon.on{background:var(--navy);border-color:var(--navy)}
.svc h4{font-size:6px;font-weight:600;margin-top:10px;line-height:1.4;min-height:17px}
.svc a{display:block;font-size:5px;color:var(--blue);margin-top:4px}
.qa{top:1132px}
.intent{top:1400px;height:300px}
.members{top:1700px;height:260px;background:var(--soft);padding-top:38px}
.member-photo{position:absolute;left:110px;top:92px;width:90px;height:90px;border-radius:50%;background:linear-gradient(135deg,#5b5e66,#1b1d22)}
.quote{position:absolute;left:240px;top:90px;width:260px}
.quote .mark{font-family:"Poppins",sans-serif;font-size:22px;color:var(--navy);line-height:1}
.quote p{font-size:5px;line-height:1.7;color:var(--muted)}
.quote b{display:block;font-size:6px;margin-top:8px}
.dots{position:absolute;left:0;right:0;top:220px;display:flex;justify-content:center;gap:4px}
.dots i{width:5px;height:5px;border-radius:50%;background:#c4c8d0}
.dots i.on{background:var(--navy)}
.newsletter{top:1960px;height:160px;text-align:center;padding-top:40px}
.signup{display:flex;justify-content:center;margin-top:16px}
.signup .field{width:200px;height:18px;border:1px solid var(--line);font-size:5px;color:var(--muted);text-align:left;padding:6px 8px}
.signup .go{width:60px;height:18px;background:var(--navy);color:var(--white);font-size:5.5px;font-family:"Poppins",sans-serif;padding-top:5px}
.footer{top:2120px;height:142px;background:var(--soft);padding:26px 40px 0}
.cols{display:flex;justify-content:space-between}
.col h4{font-size:6px;font-weight:600;margin-bottom:6px}
.col p{font-size:5px;color:var(--muted);line-height:1.9}
.social{display:flex;gap:4px}
.social i{width:9px;height:9px;border-radius:50%;background:var(--navy)}
.copyright{text-align:center;font-size:5px;color:var(--muted);margin-top:16px}
</style>
</head>
<body>
<main class="page">
  <div class="section topbar">Data-driven B2B demand generation for technology marketers</div>
  <header class="section header">
    <div class="brand">Ledgerwise Reach</div>
    <nav class="nav"><a>Home</a><a>About Us</a><a>Our Services</a><a>QA Technology</a><a>Intent Data</a><a>Testimonials</a><a>Contact Us</a></nav>
  </header>

  <section class="section hero">
    <div class="hero-art" role="img" aria-label="Abstract data visual in deep blue tones"></div>
    <div class="hero-copy">
      <h1>Ledgerwise Reach Offers Multi-Channel Demand Generation Services</h1>
      <span class="btn">Contact Us</span>
    </div>
    <div class="hero-note">Qualified leads delivered to your sales team</div>
  </section>

  <section class="section clients">
    <h2>Who we work with</h2>
    <p class="sub">We partner with leading B2B technology and data brands worldwide</p>
    <div class="stats">
      <div class="stat"><b>75,000+</b><span>Leads delivered each year</span></div>
      <div class="stat"><b>25,000+</b><span>Newsletter subscribers</span></div>
      <div class="stat"><b>50+</b><span>Global client partners</span></div>
    </div>
    <div class="logos"><span>QRT</span><span>VKD</span><span>Norvex</span><span>Brindlow</span><span>Tarvo</span><span>Prospora</span><span>Velquarion</span><span>Opal Reach</span></div>
  </section>

  <section class="section split about">
    <div class="copy" style="left:40px">
      <h3>About Us</h3>
      <p>Ledgerwise Reach is a London based B2B demand generation company. We connect technology marketers with decision makers through content syndication, newsletters and a trusted network of websites, delivering qualified leads to sales teams.</p>
      <span class="btn dark">Read More</span>
    </div>
    <div class="photo" role="img" aria-label="Overhead view of a team working at a desk with laptops" style="left:346px;background:linear-gradient(135deg,#e9ebee,#9aa0a8 55%,#3b3f46)"></div>
  </section>

  <section class="section services">
    <h2>Our Services</h2>
    <div class="svc-row">
      <div class="svc"><div class="svc-icon on"><svg width="16" height="16" viewBox="0 0 16 16"><circle cx="8" cy="8" r="6" fill="none" stroke="#fff" stroke-width="1.2"/><path d="M5 8l2 2 4-4" fill="none" stroke="#fff" stroke-width="1.2"/></svg></div><h4>Marketing Qualified Leads (MQL)</h4><a>Learn More</a></div>
      <div class="svc"><div class="svc-icon"><svg width="16" height="16" viewBox="0 0 16 16"><rect x="3" y="3" width="10" height="10" fill="none" stroke="#7a8190" stroke-width="1.2"/><path d="M5 9h6M5 6h6" stroke="#7a8190"/></svg></div><h4>Account Based Marketing Leads (ABM)</h4><a>Learn More</a></div>
      <div class="svc"><div class="svc-icon"><svg width="16" height="16" viewBox="0 0 16 16"><circle cx="8" cy="6" r="3" fill="none" stroke="#7a8190" stroke-width="1.2"/><path d="M3 14c1-3 9-3 10 0" fill="none" stroke="#7a8190" stroke-width="1.2"/></svg></div><h4>Sales Qualified Leads (SQL)</h4><a>Learn More</a></div>
    </div>
  </section>

  <section class="section split qa">
    <div class="photo" role="img" aria-label="Hand touching glowing technology icons" style="left:40px;background:linear-gradient(135deg,#0b1a3a,#1f5fae 55%,#0a1430)"></div>
    <div class="copy" style="left:336px">
      <h3>QA Technology</h3>
      <p>Every lead passes through our Prospora quality assurance platform. Contacts are verified, checked against your target profile and compliance rules before delivery, so your team only works with accurate, consented data.</p>
      <span class="btn dark">Read More</span>
    </div>
  </section>

  <section class="section split white intent">
    <div class="copy" style="left:40px;top:76px">
      <h3>Intent Data</h3>
      <p>We track research activity across our network to find accounts actively in market. Intent signals help you reach buyers at the right moment and focus spend where it drives pipeline.</p>
      <span class="btn dark">Read More</span>
    </div>
    <div class="photo" role="img" aria-label="Businessman facing a wall of digital data screens" style="left:346px;top:64px;background:linear-gradient(135deg,#2a1b4e,#3d5fb8 50%,#0c1533)"></div>
  </section>

  <section class="section members">
    <h2>Our Happy Members</h2>
    <div class="member-photo" role="img" aria-label="Portrait photo of a client"></div>
    <div class="quote">
      <div class="mark">&ldquo;</div>
      <p>Working with Ledgerwise Reach has transformed our pipeline. The leads are accurate, well qualified and delivered on time every month. Their team understands our market and our goals.</p>
      <b>Client Name</b>
      <p>Marketing Director</p>
    </div>
    <div class="dots"><i class="on"></i><i></i></div>
  </section>

  <section class="section newsletter">
    <h2>Sign Up to Our Newsletter Here</h2>
    <div class="signup"><div class="field">Enter your email address</div><div class="go">Submit</div></div>
  </section>

  <footer class="section footer">
    <div class="cols">
      <div class="col"><h4>Quick Links</h4><p>Home<br>About Us<br>Our Services<br>Contact Us</p></div>
      <div class="col"><h4>Services</h4><p>MQL Leads<br>ABM Leads<br>SQL Leads<br>Intent Data</p></div>
      <div class="col"><h4>Contact Us</h4><p>London, United Kingdom<br>www.ledgerwisereach.example<br>hello@ledgerwisereach.example</p></div>
      <div class="col"><h4>Follow Us</h4><div class="social"><i></i><i></i><i></i><i></i></div></div>
    </div>
    <div class="copyright">&copy; Ledgerwise Reach. All rights reserved.</div>
  </footer>
</main>
</body>
</html>
```